Business Card for Technology Startup

Design a 2-sided business card using the logo provided. We are a digital healthcare platform that provides a mobile app and web UI that helps caregivers, families, and doctors share information and provide better patient outcomes. We use AI and machine learning to help guide patients through their day-to-day life. The final design should communicate stability, peace, comfort, but also align with the image of an AI-driven technology startup.

I'd like the deliverable to by a Photoshop PSD file (with layers) that I can work with in pixlr.com. Should contain the following editable layers:
Name (ex. Karl Whitby)
Title (ex. Founder / CEO)
Email (ex. info@morventary.ai)
Phone (ex. (999) 482-7160)
Website (ex. https://morventary.ai)

```html
<!DOCTYPE html>
<html lang="en">
<head>
<meta charset="utf-8">
<title>Morventary Business Card</title>
<link href="https://fonts.googleapis.com/css2?family=Lato:wght@400;700;900&family=Poppins:wght@600&display=swap" rel="stylesheet">
<style>
  :root {
    --canvas: #2a2b2e;
    --card-white: #ffffff;
    --card-dark: #232325;
    --ink: #1b1b1d;
    --ink-soft: #4a4a4f;
    --accent: #0fc6ec;
    --accent-deep: #04a6e0;
    --rule: #d9dadd;
  }
  * { margin: 0; padding: 0; box-sizing: border-box; }
  html, body {
    width: 1200px; height: 952px; overflow: hidden;
    background: var(--canvas);
    font-family: "Lato", Arial, sans-serif;
  }
  .stage {
    width: 1200px; height: 952px;
    display: flex; flex-direction: column;
    align-items: center; justify-content: center; gap: 56px;
  }
  .card {
    position: relative; width: 630px; height: 360px; overflow: hidden;
    border-radius: 2px;
    box-shadow: 0 18px 40px rgba(0,0,0,.45);
  }

  /* Front */
  .card--front { background: var(--card-white); color: var(--ink); }
  .edge-band { position: absolute; background: var(--ink); width: 14px; }
  .edge-band--left { left: 0; top: 46px; height: 112px; }
  .edge-band--right { right: 0; bottom: 28px; height: 120px; }
  .divider { position: absolute; inset: 0; pointer-events: none; }

  .brand {
    position: absolute; left: 50px; top: 106px;
    display: flex; align-items: center; gap: 10px;
  }
  .brand-dot { width: 12px; height: 12px; border-radius: 50%; background: var(--accent); }
  .brand-name {
    font-family: "Poppins", Arial, sans-serif; font-weight: 600;
    font-size: 34px; letter-spacing: .3px; color: var(--ink); line-height: 1;
  }
  .address {
    position: absolute; left: 50px; bottom: 62px;
    font-size: 12.5px; color: var(--ink-soft); line-height: 1.4;
    white-space: nowrap;
  }

  .contact-block { position: absolute; left: 352px; top: 108px; }
  .person-name { font-size: 24px; letter-spacing: 1px; text-transform: uppercase; font-weight: 400; line-height: 1.15; }
  .person-name strong { font-weight: 900; }
  .person-title { font-size: 16px; color: var(--ink-soft); margin-top: 3px; letter-spacing: .3px; }
  .contact-list { list-style: none; margin-top: 14px; }
  .contact-list li {
    display: flex; align-items: center; gap: 9px;
    font-size: 15px; color: var(--ink-soft); margin-bottom: 6px;
  }
  .contact-list svg { width: 14px; height: 14px; flex: none; }

  /* Back */
  .card--back {
    background: var(--card-dark);
    display: flex; align-items: center; justify-content: center;
  }
  .brand--back { position: static; gap: 16px; }
  .brand--back .brand-name { color: #ffffff; font-size: 54px; }
  .brand--back .brand-dot { width: 20px; height: 20px; }
</style>
</head>
<body>
<main class="stage">
  <section class="card card--front" aria-label="Business card front">
    <span class="edge-band edge-band--left"></span>
    <span class="edge-band edge-band--right"></span>
    <svg class="divider" viewBox="0 0 630 360" aria-hidden="true">
      <line x1="334" y1="104" x2="312" y2="240" stroke="var(--rule)" stroke-width="1.2"/>
    </svg>

    <div class="brand">
      <span class="brand-dot"></span>
      <span class="brand-name">morventary</span>
    </div>

    <p class="address">2170 Halden Crescent Avenue, Brookfield, VT 05036</p>

    <div class="contact-block">
      <h1 class="person-name">Karl <strong>Whitby</strong></h1>
      <p class="person-title">Managing Director</p>
      <ul class="contact-list">
        <li>
          <svg viewBox="0 0 24 24" aria-hidden="true"><path fill="var(--accent)" d="M6.6 10.8a15.2 15.2 0 0 0 6.6 6.6l2.2-2.2c.3-.3.7-.4 1-.2 1.1.4 2.3.6 3.6.6.6 0 1 .4 1 1V20c0 .6-.4 1-1 1A17 17 0 0 1 3 4c0-.6.4-1 1-1h3.5c.6 0 1 .4 1 1 0 1.3.2 2.5.6 3.6.1.3 0 .7-.2 1z"/></svg>
          (999) 482-7160
        </li>
        <li>
          <svg viewBox="0 0 24 24" aria-hidden="true"><path fill="var(--accent)" d="M2 5h20v14H2z"/><path fill="none" stroke="#fff" stroke-width="1.8" d="M2.5 5.5 12 13l9.5-7.5"/></svg>
          info@morventary.ai
        </li>
        <li>
          <svg viewBox="0 0 24 24" aria-hidden="true"><circle cx="12" cy="12" r="10" fill="var(--accent)"/><path fill="none" stroke="#fff" stroke-width="1.5" d="M2 12h20M12 2c3 3 3 17 0 20M12 2c-3 3-3 17 0 20"/></svg>
          https://morventary.ai
        </li>
      </ul>
    </div>
  </section>

  <section class="card card--back" aria-label="Business card back">
    <div class="brand brand--back">
      <span class="brand-dot"></span>
      <span class="brand-name">morventary</span>
    </div>
  </section>
</main>
</body>
</html>
```